Korvane Structural Approval Standards Private Assessors

Professional Construction Consultancy Company Business Card - must keep logo colours see images below - examples have been added from my last competition - please see them as examples only!

Target Market(s)

Home Builders

Industry/Entity Type

Construction

Contact Information for Business Card

See "must haves"

Font styles to use
Sans Serif

Colors
ffffff
add136
000000

Requirements
Must have
• Daniel Moravi
• Director
• Phone: 0431 587 219
• Address: 7 Tarrunga Rd,
• Hallworth Vale, SA, 5091
• Email: korvaneassessors@mailbox-example.com
• Website: www.korvaneassessors-example.com.au
• Facebook: Korvane Structural Approval Standards
Nice to have
• Side 1: full logo
• Side 2: company details
Should not have
• hard to read
• must be clear and professional

```html
<!DOCTYPE html>
<html lang="en">
<head>
<meta charset="utf-8">
<title>Korvane Structural Approval Standards – Business Card</title>
<link rel="stylesheet" href="https://fonts.googleapis.com/css2?family=Source+Sans+3:wght@400;600;700&display=swap">
<style>
  :root {
    --ink: #000000;
    --card-black: #0b0b0b;
    --lime: #add136;
    --white: #ffffff;
    --backdrop: #e9e7e2;
  }
  * { margin: 0; padding: 0; box-sizing: border-box; }
  html, body { width: 1200px; height: 900px; overflow: hidden; }
  body {
    background: var(--backdrop);
    font-family: "Source Sans 3", "Helvetica Neue", Arial, sans-serif;
    position: relative;
  }
  .card {
    position: absolute;
    width: 540px;
    height: 320px;
    background: var(--card-black);
    border-radius: 4px;
    overflow: hidden;
    box-shadow: 0 10px 26px rgba(0,0,0,.22);
  }

  /* Side 1: company name lockup */
  .card--front { left: 90px; top: 110px; }
  .front-lockup {
    position: absolute;
    left: 0; right: 0; top: 100px;
    display: flex;
    flex-direction: column;
    align-items: center;
    color: var(--lime);
  }
  .front-lockup__row { display: flex; align-items: center; gap: 12px; }
  .front-lockup__name {
    font-weight: 700;
    font-size: 54px;
    line-height: 1;
    letter-spacing: -0.5px;
    padding-right: 12px;
    border-right: 1.5px solid var(--lime);
  }
  .front-lockup__words {
    font-weight: 600;
    font-size: 18px;
    line-height: 17px;
    text-transform: uppercase;
    letter-spacing: 0.5px;
  }
  .front-lockup__tagline {
    margin-top: 10px;
    font-weight: 600;
    font-size: 17px;
    letter-spacing: 6px;
    text-transform: uppercase;
  }

  /* Side 2: contact details */
  .card--back { left: 570px; top: 470px; }
  .back-wave { position: absolute; inset: 0; }
  .back-brand {
    position: absolute;
    right: 34px; top: 34px;
    color: var(--lime);
    font-weight: 700;
    font-size: 52px;
    line-height: 1;
    letter-spacing: -0.5px;
  }
  .person { position: absolute; left: 42px; top: 46px; }
  .person__name { color: var(--lime); font-weight: 700; font-size: 18px; }
  .person__role { color: var(--white); font-size: 14px; margin-top: 2px; padding-left: 8px; }
  .contact-list { position: absolute; left: 50px; top: 112px; list-style: none; }
  .contact-list li {
    display: flex; align-items: center; gap: 8px;
    color: var(--white); font-size: 14.5px; line-height: 21px;
  }
  .contact-list svg { width: 11px; height: 11px; flex: none; }
  .address {
    position: absolute; left: 50px; top: 200px;
    color: var(--white); font-size: 15.5px; line-height: 21px; font-style: normal;
  }
  .website {
    position: absolute; right: 20px; bottom: 22px;
    color: var(--ink); font-weight: 700; font-size: 14px;
  }
</style>
</head>
<body>
  <section class="card card--front" aria-label="Business card front">
    <div class="front-lockup">
      <div class="front-lockup__row">
        <div class="front-lockup__name">Korvane</div>
        <div class="front-lockup__words">Structural<br>Approval<br>Standards</div>
      </div>
      <div class="front-lockup__tagline">Private Assessors</div>
    </div>
  </section>

  <section class="card card--back" aria-label="Business card back">
    <svg class="back-wave" viewBox="0 0 540 320" preserveAspectRatio="none" aria-hidden="true">
      <path d="M0,262 C140,300 330,260 470,190 C330,272 160,312 0,300 Z" fill="#ffffff"/>
      <path d="M0,296 C170,306 360,262 540,156 L540,320 L0,320 Z" fill="#add136"/>
    </svg>
    <div class="back-brand">Korvane</div>
    <div class="person">
      <div class="person__name">Daniel Moravi</div>
      <div class="person__role">Director</div>
    </div>
    <ul class="contact-list">
      <li>
        <svg viewBox="0 0 12 12" aria-hidden="true"><path d="M1 4 C1 2 3 1 6 1 C9 1 11 2 11 4 L9 5 L8 3.5 L4 3.5 L3 5 Z M3 6 L9 6 L10 11 L2 11 Z" fill="#add136"/></svg>
        0431 587 219
      </li>
      <li>
        <svg viewBox="0 0 12 12" aria-hidden="true"><rect x="0.5" y="2" width="11" height="8" fill="#add136"/><path d="M0.5 2 L6 7 L11.5 2" fill="none" stroke="#0b0b0b" stroke-width="1"/></svg>
        korvaneassessors@mailbox-example.com
      </li>
      <li>
        <svg viewBox="0 0 12 12" aria-hidden="true"><rect x="0.5" y="0.5" width="11" height="11" rx="1.5" fill="#add136"/></svg>
        Korvane Structural Approval Standards
      </li>
    </ul>
    <address class="address">7 Tarrunga Rd,<br>Hallworth Vale, SA, 5091</address>
    <div class="website">www.korvaneassessors-example.com.au</div>
  </section>
</body>
</html>
```